Crest of Morning Paddocks Business Cards with logo

Need a creative business card that pops. Colorful but professional. The attached logo should be included. We are a national horse racing partnership so we are in the equine business. Nothing cartoonlike or whimsical.

Target Market(s)

professionals - 40+

Contact Information for Business Card

Maren Dunleavy
Director of Operations
27 Ashbrook Lane
Fernhollow, VT. 05912

Phone (555) 555-0147

FX: (555) 555-0192

email: maren@cmpaddocks.example
cmpaddocks.example

Requirements
Must have
• All information above should be on the business card including the website address. Professional yet creative
Nice to have
• an attention grabbing design. not boring. exciting.
Should not have
• cartoon like - whimsical.

```html
<!DOCTYPE html>
<html lang="en">
<head>
<meta charset="utf-8">
<title>Crest of Morning Paddocks – Business Card</title>
<link href="https://fonts.googleapis.com/css2?family=Cinzel:wght@600&family=Open+Sans:wght@400&display=swap" rel="stylesheet">
<style>
  :root {
    --navy: #2f3574;
    --gold: #c39530;
    --white: #ffffff;
    --text-light: #eef0f7;
    --rule: #8f93bd;
    --backdrop: #e9e6e1;
  }
  * { margin: 0; padding: 0; box-sizing: border-box; }
  html, body { width: 1200px; height: 900px; overflow: hidden; }
  body { background: var(--backdrop); position: relative; font-family: "Open Sans", sans-serif; }

  .card { position: absolute; left: 330px; width: 556px; height: 344px; }
  .card-front { top: 90px; background: var(--navy); color: var(--text-light); text-align: center; }
  .card-back { top: 469px; background: var(--white); }

  .holder-name {
    position: absolute; top: 55px; left: 0; right: 0;
    font-family: "Cinzel", serif; font-weight: 600; font-size: 22px;
    color: var(--gold); letter-spacing: 0.5px;
  }
  .holder-title { position: absolute; top: 80px; left: 0; right: 0; font-size: 16px; }

  .icon-row {
    position: absolute; top: 117px; left: 0; right: 0;
    display: flex; justify-content: center; align-items: center; gap: 4px;
  }
  .icon-row .rule { width: 38px; height: 1px; background: var(--rule); margin: 0 4px; }
  .icon { width: 20px; height: 20px; }

  .contact-list { position: absolute; top: 145px; left: 0; right: 0; font-size: 16px; line-height: 20px; list-style: none; }
  .divider { position: absolute; top: 236px; left: 191px; width: 172px; height: 1px; background: var(--rule); }
  .address { position: absolute; top: 246px; left: 0; right: 0; font-size: 16px; line-height: 20px; font-style: normal; }

  .brand-mark {
    position: absolute; left: 189px; top: 81px; width: 180px; height: 180px;
    border: 1.5px solid var(--gold); border-radius: 50%;
    display: flex; align-items: center; justify-content: center; text-align: center;
  }
  .brand-name {
    font-family: "Cinzel", serif; font-weight: 600; font-size: 19px; line-height: 26px;
    color: var(--navy); letter-spacing: 1px;
  }
</style>
</head>
<body>

<section class="card card-front">
  <h1 class="holder-name">MAREN DUNLEAVY</h1>
  <p class="holder-title">Director of Operations</p>

  <div class="icon-row">
    <span class="rule"></span>
    <svg class="icon" viewBox="0 0 20 20" aria-label="Phone"><circle cx="10" cy="10" r="9.5" fill="var(--gold)"/><path d="M5.5 8.5c0-1.5 2-2.5 4.5-2.5s4.5 1 4.5 2.5l-1.6.4-.4-1.2c-1.6-.5-3.4-.5-5 0l-.4 1.2zM7 10h6l1 4H6z" fill="var(--navy)"/></svg>
    <svg class="icon" viewBox="0 0 20 20" aria-label="Fax"><circle cx="10" cy="10" r="9.5" fill="var(--gold)"/><path d="M7 5h6v3H7zM5 8.5h10v5H13v-2H7v2H5zM7.5 12h5v3h-5z" fill="var(--navy)"/></svg>
    <svg class="icon" viewBox="0 0 20 20" aria-label="Email"><circle cx="10" cy="10" r="9.5" fill="var(--gold)"/><rect x="5" y="6.5" width="10" height="7" fill="var(--navy)"/><path d="M5 6.5l5 4 5-4" stroke="var(--gold)" stroke-width="1" fill="none"/></svg>
    <svg class="icon" viewBox="0 0 20 20" aria-label="Website"><circle cx="10" cy="10" r="9.5" fill="var(--gold)"/><circle cx="10" cy="10" r="5" fill="var(--navy)"/><path d="M5 10h10M10 5c-2 2.5-2 7.5 0 10M10 5c2 2.5 2 7.5 0 10" stroke="var(--gold)" stroke-width="0.8" fill="none"/></svg>
    <span class="rule"></span>
  </div>

  <ul class="contact-list">
    <li>(555) 555-0147</li>
    <li>(555) 555-0192</li>
    <li>maren@cmpaddocks.example</li>
    <li>www.cmpaddocks.example</li>
  </ul>

  <div class="divider"></div>

  <address class="address">27 Ashbrook Lane<br>Fernhollow, VT. 05912</address>
</section>

<section class="card card-back">
  <div class="brand-mark">
    <p class="brand-name">CREST OF<br>MORNING<br>PADDOCKS</p>
  </div>
</section>

</body>
</html>
```